Corporate Design (Wort-Bildmarke, Visitenkarten, Briefpapier, ppt-Master) für Beratungs-Start-Up
Zielgruppe
Lichtungwerk ist ein Beratungs-Start-Up und bietet Dienstleistungen im Bereich Sales- und Kommunikationsberatung.
Zielgruppe: kleine und mittelständische Unternehmen. Zunächst beschränkt sich Lichtungwerk auf Unternehmen aus dem Fahrrad- & Outdoor- beziehungsweise Uhrenfachhandel.
Beobachten steht für Lichtungwerk im Mittelpunkt. Lichtungwerk steht für Expertenwissen, nicht Besserwissen. Lichtungwerk ist Handwerk, mit einem qualitativ sehr guten, aber leicht verständlichen Ergebnis.
Stichworte für Lichtungwerk sind: offene Türen, Voraussicht, Mut, Elan, Neugier, Unangepasstheit, Optimismus, Originalität, Kreativität, Stärke, Attraktivität, Aktivität und Wandel.
Lichtungwerk ist: Energievoll, Leistungssteigernd, Beweglich, Aufbauend, (Quick)Lebendig, Greifbar, Flexibel, am Puls der Zeit.
Aufgabenstellung
Ich suche ein CD das folgende Punkte umfasst:
- Wort-/Bildmarke
- Briefpapier
- Visitenkarten (einen Vorschlag/Ansatz für einen spannenden haptischen Eindruck fände ich cool!)
- ppt-Master (inkl. Schrift und Farben) mit 3-5 Beispielsweisen (Tabellen, Graphiken, Bubbles oder ähnlichem)
Insgesamt soll das Design schnörkellos sein!
Lichtungwerk ist ein seriöser Ansatz - zwar sportlich und am Puls der Zeit. Steht aber doch eben auch für Vertrauen! Vielleicht so wie ich (siehe Bild unten!)
Im Logo sollten weder ein Fahrrad noch eine Uhr auftauchen.

```html
<!DOCTYPE html>
<html lang="de">
<head>
<meta charset="utf-8">
<title>Lichtungwerk – Briefpapier und Visitenkarten</title>
<link rel="stylesheet" href="https://fonts.googleapis.com/css2?family=Oswald:wght@400;500&family=Open+Sans:wght@400;700&family=Great+Vibes&display=swap">
<style>
  :root {
    --backdrop: #2b2b2d;
    --paper: #ffffff;
    --ink: #3a3a3a;
    --ink-soft: #555555;
    --accent: #f9bc42;
    --rule: #8a8a8a;
  }
  * { box-sizing: border-box; margin: 0; padding: 0; }
  html, body { width: 1200px; height: 849px; overflow: hidden; }
  body { background: var(--backdrop); position: relative; font-family: "Open Sans", sans-serif; color: var(--ink); }

  .letterhead {
    position: absolute; left: 130px; top: 65px; width: 508px; height: 719px;
    background: var(--paper); overflow: hidden;
  }
  .brand-mark { position: absolute; background: var(--accent); }
  .wordmark {
    position: absolute; font-family: "Oswald", sans-serif; font-weight: 500;
    color: var(--ink); letter-spacing: 0.5px; line-height: 1; white-space: nowrap;
  }
  .letterhead .brand-mark { left: 393px; top: 102px; width: 14px; height: 14px; }
  .letterhead .wordmark { right: 41px; top: 148px; font-size: 25px; }

  .sender-line {
    position: absolute; left: 55px; top: 113px; font-size: 5px;
    border-bottom: 0.6px solid var(--ink-soft); padding-right: 6px; padding-bottom: 1px; color: var(--ink-soft);
  }
  .recipient { position: absolute; left: 55px; top: 132px; font-size: 8px; line-height: 10.5px; }
  .recipient .city { margin-top: 10px; }
  .subject { position: absolute; left: 55px; top: 246px; font-size: 7.4px; font-weight: 700; }
  .body-copy { position: absolute; left: 55px; top: 274px; width: 278px; font-size: 7.2px; line-height: 9.2px; color: var(--ink-soft); }
  .body-copy p + p { margin-top: 9.2px; }
  .closing { position: absolute; left: 55px; top: 515px; font-size: 7.2px; color: var(--ink-soft); }
  .signature { position: absolute; left: 53px; top: 532px; font-family: "Great Vibes", cursive; font-size: 22px; color: #111; }

  .footer-rule { position: absolute; left: 55px; top: 663px; width: 304px; height: 0.8px; background: var(--rule); }
  .footer-col {
    position: absolute; top: 674px; font-family: "Oswald", sans-serif; font-size: 4.6px;
    line-height: 8.5px; letter-spacing: 0.5px; text-transform: uppercase; color: var(--ink);
  }
  .footer-col.company { left: 55px; }
  .footer-col.contact { left: 166px; }
  .footer-col.bank { left: 278px; }
  .bullet { display: inline-block; width: 3.5px; height: 3.5px; background: var(--accent); transform: rotate(45deg); margin-right: 3px; vertical-align: 0.3px; }

  .corner-diamond { position: absolute; background: var(--accent); transform: rotate(45deg); }
  .letterhead .corner-diamond { left: 421px; top: 633px; width: 86px; height: 86px; }

  .card { position: absolute; width: 258px; height: 166px; overflow: hidden; }
  .card-front { left: 777px; top: 189px; background: var(--paper); }
  .card-front .brand-mark { left: 40px; top: 36px; width: 14px; height: 14px; }
  .card-front .wordmark { left: 67px; top: 30px; font-size: 24px; }
  .card-details {
    position: absolute; left: 68px; top: 70px; font-family: "Oswald", sans-serif; font-size: 6.2px;
    letter-spacing: 0.6px; text-transform: uppercase; line-height: 9.4px; color: var(--ink);
  }
  .card-details .name { font-weight: 500; margin-bottom: 3px; }
  .card-details .sep { color: var(--accent); }
  .card-details .firm { margin-bottom: 3px; }
  .card-details .web { color: var(--accent); margin-top: 2px; }
  .card-front .corner-diamond { left: 214px; top: 123px; width: 37px; height: 37px; }

  .card-back { left: 777px; top: 492px; height: 167px; background: var(--accent); }
  .card-back .brand-mark { left: 122px; top: 52px; width: 14px; height: 14px; background: var(--paper); }
  .card-back .wordmark { left: 0; width: 100%; text-align: center; top: 76px; font-size: 16px; color: var(--paper); }
  .card-back .web {
    position: absolute; left: 0; width: 100%; text-align: center; top: 114px;
    font-family: "Oswald", sans-serif; font-size: 6.8px; letter-spacing: 1.6px; color: var(--paper);
  }
</style>
</head>
<body>

<section class="letterhead" aria-label="Briefpapier">
  <span class="brand-mark"></span>
  <div class="wordmark">LICHTUNGWERK</div>

  <div class="sender-line">Vorname Nachname, Musterstr. 123, 12345 Musterstadt</div>
  <address class="recipient" style="font-style:normal">
    <div>Martina Musterfrau</div>
    <div>Musterstraße 456</div>
    <div class="city">12345 Berlin</div>
  </address>

  <div class="subject">Quidero molore, atatur sae. Nequat,</div>
  <div class="body-copy">
    <p>Ur sit, imus, ipicatem voluptate eum re dolluptios sequosam, eum reritati am volor sapedissi quo blaboribust, sequass itasped igendi cus exerfer feruptas iusanda ndaest, qui omnis nus aut fugitinis quatur ad ullaut mostem quasperiae corem et aciatem illatin ciduntores quidis utemquam autemperae soluptiae lab illacescia solorum et fugiam ratatatus exerro blaciis samusam etur? Uga. Neque nam simi, nest, ommod essedios magnatia nossi aute nonsequam fugiaspis moluptas sed el int etur saepe nonsecatem excea noneceperrum ulligendit faccullores et lantur si ium at.Ota cuptae non ea de opta voles rem rae dolore ilia vellab isi blanis idit veribus auda alit labore desenis imenis que in con rehent, explat ped que volorum, autent, si tetur?</p>
    <p>Ihil ium restior ecepero reptistius es aborepe diatiunt dignis diciae voluptu ribearit, que nat aute et as maximus, qui blab iur aut volest, nonsequae odios doluptatiae velignimin perescia vent.<br>Pa voluptas expero corectur molest eaquid enda vidus verciis quodi te dit aliquid unturem poreper feratur? Quis aut rehenihilit et quam, eris et perorru mquamusa quo et untia volupie nisimoluptae esseribus cora doluptati doluptatur atisciumqui re pa quat aut lam solescia intiis et millabor sit odis et quos re sam, vendicientur abo. Equi totatus rest, nosam quodi omni doloriosam des ea nimpelique volo elendae dellign ihilitis solupta temporp orupta iuntia ipiste natibusapis volesedis reriori taerrup tatiberes nobitiur, sequi omnihillab id maximagnat omnimus dolo quunt, int aut earum lacit peliquunt iduciet, id que autemolum deruptati te non re.</p>
  </div>
  <div class="closing">Sincerely</div>
  <div class="signature">M. Mmann</div>

  <div class="footer-rule"></div>
  <div class="footer-col company">Musterfirma GmbH<br>Musterstr. 123<br>12345 Musterstadt</div>
  <div class="footer-col contact"><span class="bullet"></span>010 / 234 567 89<br><span class="bullet"></span>010 / 234 567 90<br><span class="bullet"></span>info@musterweb.de</div>
  <div class="footer-col bank">Musterbank AG<br>IBAN: DE12 3456 7890 1234<br>BIC: ABC456789</div>

  <span class="corner-diamond"></span>
</section>

<section class="card card-front" aria-label="Visitenkarte Vorderseite">
  <span class="brand-mark"></span>
  <div class="wordmark">LICHTUNGWERK</div>
  <div class="card-details">
    <div class="name">Max Mustermann <span class="sep">•</span> Geschäftsführer</div>
    <div>Musterfirma GmbH</div>
    <div class="firm">Musterstr. 123 <span class="sep">•</span> 12345 Musterstadt</div>
    <div><span class="bullet"></span>010 / 234 567 89 &nbsp;<span class="bullet"></span>010 / 234 567 90</div>
    <div><span class="bullet"></span>info@lichtungwerk.de</div>
    <div class="web">www.lichtungwerk.de</div>
  </div>
  <span class="corner-diamond"></span>
</section>

<section class="card card-back" aria-label="Visitenkarte Rückseite">
  <span class="brand-mark"></span>
  <div class="wordmark">LICHTUNGWERK</div>
  <div class="web">WWW.LICHTUNGWERK.DE</div>
</section>

</body>
</html>
```